Niche Apparel business needs Vendaloo Site Design

Small apparel business needs design for a vendaloo website to move math & science themed clothes. All designs for clothing will be based around simple, sleek plots that are derived from math concepts (fractals, choas, etc.) Initially we will focus exclusively on shirts, but we may expand to other clothing types soon.

The intent of the site is to showcase the simple designs on our products and how they can appeal to math & science minded, but in a subtle and fashionable way. We don't want to scream "I LOVE MATH" - rather, we design items who show off beautiful, mathematically-derived motifs and patterns. Those in the know will appreciate where the designs come, those who don't know the math will simply see a cool design (I.e. https://en.lorvexa.org/wiki/Dragon_curve).

Target Market(s)

Math & Science interested people, primarily upper middle class with disposable income for novelty or niche clothing.

Font styles to use
Serif

Requirements
Should not have
• Profanity, previously copywrited material, or proprietary content in any way.

```html
<!DOCTYPE html>
<html lang="en">
<head>
<meta charset="utf-8">
<title>Sinewear — Math &amp; Science Apparel</title>
<link rel="stylesheet" href="https://fonts.googleapis.com/css2?family=Exo+2:wght@300;400;500;600;700&family=Kaushan+Script&display=swap">
<style>
:root{
  --green:#1b9a4f;
  --green-dark:#158043;
  --ink:#1d1d1d;
  --text:#3a3a3a;
  --muted:#6b6b6b;
  --line:#e3e3e3;
  --soft:#f5f6f8;
  --white:#ffffff;
}
*{box-sizing:border-box;margin:0;padding:0}
html,body{width:1200px;height:2997px;overflow:hidden}
body{font-family:"Exo 2",sans-serif;color:var(--text);background:var(--white);position:relative}
.abs{position:absolute}
a{color:inherit;text-decoration:none}

/* top bar */
.topbar{left:0;top:0;width:1200px;height:33px;background:var(--green);color:var(--white);font-size:12px}
.topbar .phone{left:160px;top:9px;display:flex;align-items:center;gap:6px}
.topbar .promo{left:0;width:1200px;top:9px;text-align:center}
.topbar .promo u{margin-left:3px}
.topbar .social{right:160px;top:8px;display:flex;gap:5px}
.sq{width:16px;height:16px;border-radius:3px;background:var(--white);opacity:.9;display:block}

/* header */
.brand{font-weight:700;color:var(--green);letter-spacing:-.5px}
.header .brand{left:160px;top:58px;font-size:40px}
.nav{right:160px;top:82px;display:flex;align-items:center;gap:26px;font-size:13px;color:var(--ink);text-transform:uppercase}
.nav .active{position:relative}
.nav .active:after{content:"";position:absolute;left:0;right:0;bottom:-6px;height:2px;background:var(--green)}
.cart{position:relative;display:flex;align-items:center;gap:10px;font-size:17px}
.cart .badge{position:absolute;left:12px;top:-10px;width:13px;height:13px;border-radius:50%;background:var(--green);color:var(--white);font-size:9px;text-align:center;line-height:13px}

/* hero */
.hero{left:0;top:146px;width:1200px;height:420px;background:linear-gradient(90deg,#5a5550 0%,#7a4a4f 20%,#8b7f92 38%,#6d6e73 55%,#4b5a66 75%,#3a4a58 100%)}
.hero .shade{left:0;top:0;width:1200px;height:420px;background:linear-gradient(180deg,rgba(60,60,60,.55) 0%,rgba(0,0,0,0) 40%,rgba(0,0,0,.2) 100%)}
.hero .script{left:676px;top:106px;font-family:"Kaushan Script",cursive;font-size:44px;color:var(--white)}
.hero h1{left:670px;top:152px;font-size:50px;font-weight:700;color:var(--white);letter-spacing:-.5px}
.hero p{left:674px;top:212px;width:340px;font-size:14px;line-height:21px;color:var(--white)}
.btn{display:inline-flex;align-items:center;justify-content:center;background:var(--green);color:var(--white);border-radius:20px;font-size:14px;font-weight:500}
.hero .btn{left:674px;top:275px;width:127px;height:36px}
.slide-arrow{width:30px;height:30px;background:var(--white);border-radius:3px;display:flex;align-items:center;justify-content:center}
.hero .prev{left:30px;top:196px}
.hero .next{right:30px;top:196px}

/* shop */
.section-title{font-size:38px;font-weight:500;color:var(--ink)}
.shop-title{left:160px;top:612px}
.tabs{right:160px;top:623px;display:flex;align-items:center;gap:16px;font-size:14px;color:var(--ink)}
.tabs .on{background:var(--green);color:var(--white);border-radius:14px;padding:4px 20px}
.product{width:203px;height:262px;border:1px solid var(--line);background:var(--white)}
.product.focus{border:2px solid var(--green)}
.product .shirt{position:absolute;left:26px;top:40px;width:150px;height:175px;border-radius:30px 30px 6px 6px}
.product .tool{position:absolute;right:12px;width:24px;height:24px;border-radius:3px;display:flex;align-items:center;justify-content:center}
.product .tool.add{top:12px;background:var(--green)}
.product .tool.look{top:48px;background:#f1f1f1}
.p-info{width:203px;text-align:center}
.p-info .name{font-size:16px;color:var(--ink)}
.p-info .price{font-size:14px;color:var(--green);margin-top:2px}
.viewall{left:536px;top:1349px;width:128px;height:37px}

/* newsletter */
.news-band{left:0;top:1485px;width:1200px;height:302px;background:linear-gradient(90deg,#7a4a1e 0%,#c9862f 25%,#e1a448 45%,#6b3a22 70%,#3a1a1c 85%,#5c1e24 100%)}
.news-box{left:570px;top:1436px;width:468px;height:309px;background:var(--green);color:var(--white);padding:42px 52px}
.news-box .pre{font-size:24px;font-weight:400}
.news-box h2{font-size:38px;font-weight:700;line-height:42px;margin-top:2px}
.news-box p{font-size:14px;line-height:20px;margin-top:10px;width:330px}
.news-box .field{margin-top:12px;width:320px;height:36px;background:var(--white);border-radius:18px;color:#9a9a9a;font-size:11px;font-style:italic;padding:12px 14px}
.news-box .sub{margin-top:20px;width:117px;height:37px;background:var(--white);color:var(--ink);border-radius:19px;font-size:14px;display:flex;align-items:center;justify-content:center}

/* testimonials */
.t-title{left:0;width:1200px;top:1840px;text-align:center}
.t-arrow{width:30px;height:30px;background:var(--green);border-radius:2px;display:flex;align-items:center;justify-content:center}
.quote{width:280px;height:113px;background:var(--white);border-left:2px solid var(--green);box-shadow:0 1px 6px rgba(0,0,0,.1);padding:22px 14px;font-size:12px;line-height:18px;color:var(--muted)}
.quote:after{content:"";position:absolute;left:36px;bottom:-14px;border-left:10px solid transparent;border-right:10px solid transparent;border-top:14px solid var(--green);transform:skewX(30deg)}
.person{display:flex;align-items:center;gap:12px}
.avatar{width:60px;height:60px;border-radius:50%;border:2px solid var(--green);background:linear-gradient(135deg,#b08a74,#5e4638)}
.person .nm{font-size:15px;color:var(--ink)}
.person .rl{font-size:12px;color:var(--green)}
.person .st{font-size:11px;color:#f2b01e;letter-spacing:1px}

/* news */
.news-area{left:0;top:2162px;width:1200px;height:614px;background:var(--soft)}
.n-title{left:0;width:1200px;top:2202px;text-align:center}
.post{width:278px;height:422px;background:var(--white)}
.post .img{height:223px}
.post .body{padding:16px 20px}
.post .date{font-size:11px;color:var(--green)}
.post h3{font-size:18px;font-weight:500;color:var(--ink);margin-top:4px}
.post p{font-size:11px;line-height:16.5px;color:var(--muted);margin-top:12px}
.post .more{display:flex;align-items:center;gap:10px;margin-top:18px;font-size:14px;color:var(--ink)}
.plus{width:27px;height:27px;border-radius:50%;background:var(--green);color:var(--white);display:flex;align-items:center;justify-content:center;font-size:18px;font-weight:600}

/* footer */
.footer .brand{left:0;width:1200px;text-align:center;top:2812px;font-size:44px}
.f-links{left:0;width:1200px;text-align:center;top:2897px;font-size:11px;color:var(--text)}
.f-social{left:550px;top:2918px;display:flex;gap:6px}
.f-social .sq{width:20px;height:20px;background:var(--green);opacity:1}
.f-line{left:160px;top:2953px;width:880px;height:1px;background:var(--line)}
.cards{right:160px;top:2965px;display:flex;gap:4px}
.card{width:34px;height:22px;border-radius:3px;background:#e8e8ea;border:1px solid #d5d5d8}
</style>
</head>
<body>

<div class="abs topbar">
  <div class="abs phone">
    <svg width="14" height="14" viewBox="0 0 24 24" fill="none" stroke="#fff" stroke-width="2"><circle cx="12" cy="12" r="10"/><path d="M8.5 7.5c0 4 4 8 8 8l1-2-2.5-1.5-1.2 1.2c-1.5-.7-2.8-2-3.5-3.5L11.5 8.5 10 6z" fill="#fff" stroke="none"/></svg>
    (123) 456-7890
  </div>
  <div class="abs promo">Summer sale discount off 20%! <u>Shop Now</u></div>
  <div class="abs social"><span class="sq"></span><span class="sq"></span><span class="sq"></span><span class="sq"></span></div>
</div>

<header class="header">
  <div class="abs brand">Sinewear</div>
  <nav class="abs nav">
    <a class="active">Home</a><a>Products</a><a>About Us</a><a>Contact</a>
    <svg width="16" height="16" viewBox="0 0 24 24" fill="none" stroke="#222" stroke-width="2"><circle cx="10" cy="10" r="7"/><path d="M15 15l6 6"/></svg>
    <span class="cart">
      <svg width="18" height="18" viewBox="0 0 24 24" fill="none" stroke="#222" stroke-width="2"><path d="M2 3h3l3 12h11l2-8H6"/><circle cx="9" cy="20" r="1.5"/><circle cx="18" cy="20" r="1.5"/></svg>
      <span class="badge">0</span>$0.00
    </span>
  </nav>
</header>

<section class="abs hero">
  <div class="abs shade" role="img" aria-label="Photo of shirts hanging on a clothes rail"></div>
  <div class="abs script">This Summer</div>
  <h1 class="abs">New Collection</h1>
  <p class="abs">Lorem ipsum dolor sit amet, consectetur adipisicing elit, sed do eiusmod tempor incididunt.</p>
  <a class="abs btn">Shop Now &rsaquo;</a>
  <div class="abs slide-arrow prev"><svg width="10" height="14" viewBox="0 0 10 14" fill="none" stroke="#222" stroke-width="1.6"><path d="M7 2L2 7l5 5"/></svg></div>
  <div class="abs slide-arrow next"><svg width="10" height="14" viewBox="0 0 10 14" fill="none" stroke="#222" stroke-width="1.6"><path d="M3 2l5 5-5 5"/></svg></div>
</section>

<h2 class="abs section-title shop-title">Our Shop</h2>
<div class="abs tabs"><span class="on">All</span><span>New Arrivals</span><span>Best Sellers</span></div>

<div class="abs product focus" style="left:160px;top:676px">
  <div class="shirt" style="background:#a6a6a8" role="img" aria-label="Grey math print t-shirt"></div>
  <span class="tool add"><svg width="14" height="14" viewBox="0 0 24 24" fill="none" stroke="#fff" stroke-width="2"><path d="M2 3h3l3 12h11l2-8H6"/><circle cx="9" cy="20" r="1.5"/><circle cx="18" cy="20" r="1.5"/></svg></span>
  <span class="tool look"><svg width="13" height="13" viewBox="0 0 24 24" fill="none" stroke="#333" stroke-width="2"><circle cx="10" cy="10" r="7"/><path d="M15 15l6 6"/></svg></span>
</div>
<div class="abs product" style="left:386px;top:676px"><div class="shirt" style="background:#f1f1f1" role="img" aria-label="White equations print t-shirt"></div></div>
<div class="abs product" style="left:611px;top:676px"><div class="shirt" style="background:#8ec6e8" role="img" aria-label="Light blue graph joke t-shirt"></div></div>
<div class="abs product" style="left:836px;top:676px"><div class="shirt" style="background:#3d4560" role="img" aria-label="Navy triangles t-shirt"></div></div>
<div class="abs p-info" style="left:160px;top:949px"><div class="name">Lorem Ipsum Dolor</div><div class="price">$29.99</div></div>
<div class="abs p-info" style="left:386px;top:949px"><div class="name">Lorem Ipsum Dolor</div><div class="price">$29.99</div></div>
<div class="abs p-info" style="left:611px;top:949px"><div class="name">Lorem Ipsum Dolor</div><div class="price">$29.99</div></div>
<div class="abs p-info" style="left:836px;top:949px"><div class="name">Lorem Ipsum Dolor</div><div class="price">$29.99</div></div>

<div class="abs product" style="left:160px;top:1007px"><div class="shirt" style="background:#d0152c" role="img" aria-label="Red absolute value t-shirt"></div></div>
<div class="abs product" style="left:386px;top:1007px"><div class="shirt" style="background:#0e4c9a" role="img" aria-label="Royal blue summation t-shirt"></div></div>
<div class="abs product" style="left:611px;top:1007px"><div class="shirt" style="background:#141414" role="img" aria-label="Black physics diagram t-shirt"></div></div>
<div class="abs product" style="left:836px;top:1007px"><div class="shirt" style="background:#5a6160" role="img" aria-label="Charcoal function plots t-shirt"></div></div>
<div class="abs p-info" style="left:160px;top:1281px"><div class="name">Lorem Ipsum Dolor</div><div class="price">$29.99</div></div>
<div class="abs p-info" style="left:386px;top:1281px"><div class="name">Lorem Ipsum Dolor</div><div class="price">$29.99</div></div>
<div class="abs p-info" style="left:611px;top:1281px"><div class="name">Lorem Ipsum Dolor</div><div class="price">$29.99</div></div>
<div class="abs p-info" style="left:836px;top:1281px"><div class="name">Lorem Ipsum Dolor</div><div class="price">$29.99</div></div>

<a class="abs btn viewall">View All &rsaquo;</a>

<div class="abs news-band" role="img" aria-label="Photo of clothes on wooden hangers"></div>
<div class="abs news-box">
  <div class="pre">Subscribe Our</div>
  <h2>Newsletter</h2>
  <p>Subscribe to our newsletter and be the first to learn about new arrivals, sales, and promos!</p>
  <div class="field">Your Email Here*</div>
  <div class="sub">Subscribe Now &rsaquo;</div>
</div>

<h2 class="abs section-title t-title">Testimonials</h2>
<div class="abs t-arrow" style="left:160px;top:1855px"><svg width="10" height="14" viewBox="0 0 10 14" fill="none" stroke="#fff" stroke-width="1.6"><path d="M7 2L2 7l5 5"/></svg></div>
<div class="abs t-arrow" style="left:1009px;top:1855px"><svg width="10" height="14" viewBox="0 0 10 14" fill="none" stroke="#fff" stroke-width="1.6"><path d="M3 2l5 5-5 5"/></svg></div>

<div class="abs quote" style="left:160px;top:1918px">Lorem ipsum dolor sit amet, consectetur adipisicing elit, sed do eiusmod tempor incididunt ut labore et dolore magna aliqua. Ut enim ad minim veniam.</div>
<div class="abs quote" style="left:461px;top:1918px">Lorem ipsum dolor sit amet, consectetur adipisicing elit, sed do eiusmod tempor incididunt ut labore et dolore magna aliqua. Ut enim ad minim veniam.</div>
<div class="abs quote" style="left:761px;top:1918px">Lorem ipsum dolor sit amet, consectetur adipisicing elit, sed do eiusmod tempor incididunt ut labore et dolore magna aliqua. Ut enim ad minim veniam.</div>

<div class="abs person" style="left:160px;top:2058px"><div class="avatar" role="img" aria-label="Customer portrait"></div><div><div class="nm">Merry Smith</div><div class="rl">Customer</div><div class="st">★★★★★</div></div></div>
<div class="abs person" style="left:461px;top:2058px"><div class="avatar" role="img" aria-label="Customer portrait"></div><div><div class="nm">John Doe</div><div class="rl">Customer</div><div class="st">★★★★★</div></div></div>
<div class="abs person" style="left:761px;top:2058px"><div class="avatar" role="img" aria-label="Customer portrait"></div><div><div class="nm">Jane Doe</div><div class="rl">Customer</div><div class="st">★★★★★</div></div></div>

<div class="abs news-area"></div>
<h2 class="abs section-title n-title">News &amp; Updates</h2>

<article class="abs post" style="left:160px;top:2276px">
  <div class="img" style="background:linear-gradient(90deg,#6b5a4c,#c8141f 20%,#c8141f 80%,#6b5a4c)" role="img" aria-label="Red pi t-shirt on wooden background"></div>
  <div class="body"><div class="date">June 05, 2021</div><h3>Lorem Ipsum Dolor</h3><p>Lorem ipsum dolor sit amet, consectetur adipisicing elit, sed do eiusmod tempor incididunt ut labore et dolore magna aliqua. Ut enim ad minim veniam...</p><div class="more">Read More <span class="plus">+</span></div></div>
</article>
<article class="abs post" style="left:461px;top:2276px">
  <div class="img" style="background:linear-gradient(90deg,#e8e8e8,#2a2a2a 25%,#2a2a2a 75%,#e8e8e8)" role="img" aria-label="Black trigonometry pun t-shirt worn on model"></div>
  <div class="body"><div class="date">June 05, 2021</div><h3>Lorem Ipsum Dolor</h3><p>Lorem ipsum dolor sit amet, consectetur adipisicing elit, sed do eiusmod tempor incididunt ut labore et dolore magna aliqua. Ut enim ad minim veniam...</p><div class="more">Read More <span class="plus">+</span></div></div>
</article>
<article class="abs post" style="left:761px;top:2276px">
  <div class="img" style="background:linear-gradient(90deg,#c9c9cb,#3a3c48 20%,#3a3c48 80%,#c9c9cb)" role="img" aria-label="Dark grey heart of formulas t-shirt worn on model"></div>
  <div class="body"><div class="date">June 05, 2021</div><h3>Lorem Ipsum Dolor</h3><p>Lorem ipsum dolor sit amet, consectetur adipisicing elit, sed do eiusmod tempor incididunt ut labore et dolore magna aliqua. Ut enim ad minim veniam...</p><div class="more">Read More <span class="plus">+</span></div></div>
</article>

<footer class="footer">
  <div class="abs brand">Sinewear</div>
  <div class="abs f-links">Privacy Policy &nbsp;|&nbsp; Terms &amp; Conditions</div>
  <div class="abs f-social"><span class="sq"></span><span class="sq"></span><span class="sq"></span><span class="sq"></span></div>
  <div class="abs f-line"></div>
  <div class="abs cards"><span class="card"></span><span class="card"></span><span class="card"></span><span class="card"></span></div>
</footer>

</body>
</html>
```